Simple and clean poster/flyer design needed for public speaker!

SIMPLE AND CLEAN DESIGN NEEDED FOR POSTER/FLYER

I AM a public speaker based in London (www.corvanlethby.com)
and I would like to have a custom-made flyer/poster
(preferably in adobe CS4 template format) that I con customize (just changing the text) for my various speeches, topics and locations

I am looking for something very simple and clean.
NO extravagance or crowded poster, but a rather beautiful clean and eye-catching design that clearly informs people what i am talking about, where and when.

Go to my website www.corvanlethby.com
to see the colour scheme and style that I like
my poster should be like the website, similar colours, logo, clean, simple and clear.

Summary

(1) simple and clean design
(2) design that fits my brand (see website)
(3) clear and eye-catching to promote my speeches
(4) customizable for my various talks, by simply chancing the text (Please Adobe Photoshop CS4 template format)
(5)in A3, A4, A5, A6 sizes, so i can use it for both flyers and small posters

ADDITIONS

BIG BOLD HEADLINE TO GRAP ATTENTION, greatest prominence

sub headline to explain, smaller than the headline, but still prominent on the poster

just a few bullet points to list the benefits and answer the “whats in for me”-question
this is for people who are already interested and continue reading, medium prominence.

WHERE, WHEN, HOW MUCH-information, in the lower section of the poster, little text, but clearly visible

only one point of CONTACT on my poster “www.corvanlethby.com”, bit big and clear so that it is very prominent

little text, effectively used
LESS IS MORE
Updates

contact me regarding logo files and any questions you may have!

for the logo files go to

https://share.dropvaultex.net/f/x.aspx?k=41c07d2e9ab35f18c6d2

click on the folder "logo pack" to see the files

thanks for your interest. hope to see great designs!
I am really looking forward to it
if you have any questions, please do not hesitate to ask

Kind Regards
Corvan
 

• Simple, clean design, text sparingly used.

• The mood should be light-hearted, calm, bright, simple and friendly, comic like

• a lot of white space, calling more attention to the content

• a light blue, dark blue, white and black colour scheme as seen on the homepage (www.corvanlethby.com) please use the exact same colours as seen on the homepage.

White being most predominant, 2 different blue used to highlight something, black for text on white background.

• One graphic would be cool, as long as it is blue. It could be waves-like graphic, or something like the white pattern in the background, in my case just in blue on white background > http://www.quillmereretreathouse.org/., I do not mean exactly this graphic and not that crowded but a simple single graphic in blue as long as it fits the theme and feel of my poster

Top o f the poster

• (a )One short bold headline (TALK TITLE) with a sub-headline below it (hook)

• or (b) headline as question (…....?) and below sub-headline offering the solution (my talk ;-) of course)

• 3 benefits as on homepage, that I can adapt for each talk (bottom right of my start site “what are you looking for?” either blue on white, or as in the page white on blue...whatever looks better and fits the design). Not sure how that looks, and if to include it!

• the bottom of the poster will have “Where”-information “when”-information “ticket price” info

• contact at the very bottom...for more into or to purchase tickets (my website and email)

If you have any questions or need clarification please write me!

Requirements
Must have
• lot of white space
• less is more - simple design
• little text, little graphics- only used when necessary to greatest effect.
• light, friendly, modern feel
• blue-color scheme

```html
<!DOCTYPE html>
<html lang="en">
<head>
<meta charset="utf-8">
<title>Corvan Lethby – Talk Poster</title>
<link rel="stylesheet" href="https://fonts.googleapis.com/css2?family=Open+Sans:wght@600;700;800&display=swap">
<style>
  :root {
    --ink: #1f2b3a;
    --ink-soft: #2a3848;
    --black: #111111;
    --white: #ffffff;
    --sky: #7cc3da;
    --sky-pale: #e3f1f5;
    --sky-mist: #eef7fa;
    --teal: #4e97ab;
    --teal-deep: #3c7f93;
    --band-top: #86c3d8;
    --band-light: #b7dde9;
    --band-mid: #9fd0e1;
    --bullet: #c9d8de;
  }
  * { margin: 0; padding: 0; box-sizing: border-box; }
  html, body { width: 848px; height: 1200px; overflow: hidden; background: var(--white); }
  body { font-family: "Open Sans", Arial, sans-serif; color: var(--ink); }

  .poster { position: relative; width: 848px; height: 1200px; overflow: hidden; background: var(--white); }

  .hero-figure {
    position: absolute; left: 560px; top: 0; width: 288px; height: 500px;
    background: radial-gradient(ellipse at 55% 40%, #c5e3ee 0%, #e2f1f6 45%, rgba(255,255,255,0) 75%);
  }
  .dot-field {
    position: absolute; left: 0; top: 600px; width: 848px; height: 370px;
    background: linear-gradient(180deg, rgba(255,255,255,0) 0%, #e6f3f8 35%, #d6ecf4 100%);
  }

  .headline {
    position: absolute; top: 128px; left: 0; width: 848px; text-align: center;
    font-weight: 800; font-size: 55px; line-height: 58px; letter-spacing: -0.5px;
    color: var(--ink);
    text-shadow: 2px 2px 0 var(--sky);
  }
  .subheadline {
    position: absolute; top: 285px; left: 0; width: 848px; text-align: center;
    font-weight: 700; font-size: 31px; line-height: 44px; color: var(--ink-soft);
  }

  .benefits {
    position: absolute; left: 26px; top: 493px; width: 796px; height: 302px;
    background: var(--sky-pale); border-radius: 26px;
    box-shadow: -2px 3px 0 var(--sky);
    list-style: none; padding-top: 42px;
  }
  .benefit {
    display: flex; align-items: center; height: 80px; padding-left: 52px;
    font-weight: 700; font-size: 29px; color: var(--black);
  }
  .benefit-number {
    width: 54px; height: 54px; border-radius: 50%; background: var(--bullet);
    display: flex; align-items: center; justify-content: center;
    font-size: 26px; font-weight: 800; color: var(--ink); margin-right: 14px;
  }

  .book-badge { position: absolute; left: 590px; top: 745px; width: 240px; height: 240px; }
  .book-text {
    position: absolute; left: 612px; top: 818px; width: 200px; color: var(--white);
  }
  .book-title { font-weight: 800; font-size: 28px; line-height: 32px; text-shadow: 1px 1px 0 var(--teal-deep); }
  .book-code-label { font-weight: 700; font-size: 13px; line-height: 16px; margin-top: 4px; padding-left: 20px; }
  .book-code { font-weight: 800; font-size: 19px; line-height: 20px; padding-left: 20px; }

  .event-band {
    position: absolute; left: 0; top: 967px; width: 848px; height: 165px;
    background: linear-gradient(180deg, var(--band-top) 0px, var(--band-top) 14px, var(--band-light) 14px, var(--band-mid) 100%);
  }
  .event-col { position: absolute; top: 24px; }
  .event-col--where { left: 45px; }
  .event-col--when { left: 286px; }
  .event-col--price { left: 623px; }
  .event-label { font-weight: 700; font-size: 21px; color: var(--ink); line-height: 26px; }
  .event-venue { font-weight: 800; font-size: 35px; line-height: 33px; color: var(--white); margin-top: 6px; }
  .event-city { font-weight: 700; font-size: 20px; color: var(--white); line-height: 24px; }
  .event-date { font-weight: 800; font-size: 34px; color: var(--ink); margin-top: 16px; line-height: 40px; }
  .event-year { font-weight: 700; font-size: 19px; color: var(--white); margin-top: 6px; }
  .event-price { font-weight: 800; font-size: 32px; color: var(--ink); margin-top: 16px; line-height: 40px; }

  .contact {
    position: absolute; left: 0; top: 1136px; width: 848px; text-align: center; color: var(--black);
  }
  .contact-lead { font-weight: 700; font-size: 17px; line-height: 22px; }
  .contact-url { font-weight: 800; font-size: 28px; line-height: 36px; color: var(--ink); }
  .contact-url-name { color: var(--sky); }
</style>
</head>
<body>
<main class="poster">
  <div class="hero-figure" role="img" aria-label="Light blue stylised figure with arms raised amid radiating light rays"></div>
  <div class="dot-field" role="img" aria-label="Soft light blue halftone dot pattern with flowing white wave swooshes"></div>

  <h1 class="headline">What are you looking for?<br>semper quis suscipit</h1>
  <p class="subheadline">Fusce justo nunc, semper quis<br>suscipit nec, aliquam ac eros.</p>

  <ol class="benefits">
    <li class="benefit"><span class="benefit-number">1</span>improved self-esteem</li>
    <li class="benefit"><span class="benefit-number">2</span>inner peace and calm</li>
    <li class="benefit"><span class="benefit-number">3</span>greater purpose and meaning in life</li>
  </ol>

  <svg class="book-badge" viewBox="0 0 240 240" aria-hidden="true">
    <defs>
      <linearGradient id="badgeFill" x1="0" y1="0" x2="0" y2="1">
        <stop offset="0" stop-color="#6db1c4"/>
        <stop offset="1" stop-color="#3d8396"/>
      </linearGradient>
      <linearGradient id="curlFill" x1="0" y1="0" x2="1" y2="1">
        <stop offset="0" stop-color="#ffffff"/>
        <stop offset="1" stop-color="#cfd6d9"/>
      </linearGradient>
    </defs>
    <path d="M122 2 A117 117 0 1 0 208 204 L180 150 Z" fill="url(#badgeFill)"/>
    <path d="M122 2 A117 117 0 0 1 232 150 L180 150 L208 204 A117 117 0 0 1 122 2 Z" fill="none"/>
    <path d="M122 2 A117 117 0 0 1 236 118 Q238 150 226 170 L180 150 Z" fill="url(#badgeFill)"/>
    <path d="M226 170 Q200 150 180 150 Q176 190 196 222 Q214 196 226 170 Z" fill="url(#curlFill)"/>
  </svg>
  <div class="book-text">
    <div class="book-title">BOOK NOW</div>
    <div class="book-code-label">promotional code</div>
    <div class="book-code">FREETICKET</div>
  </div>

  <section class="event-band">
    <div class="event-col event-col--where">
      <div class="event-label">Where</div>
      <div class="event-venue">Halden<br>Arena</div>
      <div class="event-city">London</div>
    </div>
    <div class="event-col event-col--when">
      <div class="event-label">When</div>
      <div class="event-date">03 September</div>
      <div class="event-year">2010</div>
    </div>
    <div class="event-col event-col--price">
      <div class="event-label">Ticket price</div>
      <div class="event-price">£ --</div>
    </div>
  </section>

  <footer class="contact">
    <p class="contact-lead">For more information or to book your ticket, visit</p>
    <p class="contact-url">www.<span class="contact-url-name">corvan</span>lethby.com</p>
  </footer>
</main>
</body>
</html>
```